Bright Willow Wellness
Heal your Body Mind and Spirit
Bright Willow Wellness - Health
Creative Brief
Professional
Melora T. Grant, MSW, LSW
Health Consultant and Spiritual Counselor
Certifications: Feeling Map Form Key Spiritual Counseling
melora@brightwillowwellness.example
www.brightwillowwellness.example
Next appointment: _____________________________________
guest guest
where is the logo
mgrant417 mgrant417
Designers: Please only design for business cards, not stationary. Thanks...

```html
<!DOCTYPE html>
<html lang="en">
<head>
<meta charset="utf-8">
<title>Bright Willow Wellness — Business Card</title>
<link rel="stylesheet" href="https://fonts.googleapis.com/css2?family=Cinzel:wght@400;600&family=Cormorant+Garamond:ital,wght@1,600&family=Open+Sans:ital,wght@0,400;0,700;1,400&display=swap">
<style>
  :root {
    --bg: #e6e8eb;
    --card: #ffffff;
    --navy: #16234f;
    --navy-deep: #0f1a3e;
    --teal: #2f6f8f;
    --sky: #8fc0d6;
    --sky-pale: #c9e2ec;
    --ink: #2a2a2a;
    --rule: #555555;
  }
  * { box-sizing: border-box; margin: 0; padding: 0; }
  html, body {
    width: 1200px; height: 980px; overflow: hidden;
    background: var(--bg);
  }
  .canvas {
    width: 1200px; height: 980px;
    display: flex; flex-direction: column; align-items: center; justify-content: center;
    gap: 40px;
  }
  .card {
    position: relative;
    width: 760px; height: 434px;
    background: var(--card);
    border-radius: 22px;
    overflow: hidden;
    box-shadow: 0 2px 10px rgba(0,0,0,0.12);
  }

  /* Front */
  .card-front .wave { position: absolute; inset: 0; width: 100%; height: 100%; }
  .brand {
    position: absolute; left: 150px; top: 92px;
    display: flex; align-items: center; gap: 22px;
  }
  .brand-mark {
    width: 74px; height: 74px; border-radius: 50%;
    background: var(--teal);
    flex: none;
  }
  .brand-name {
    font-family: "Cinzel", serif; font-weight: 600;
    font-size: 34px; letter-spacing: 1px; color: var(--navy);
    line-height: 1;
  }
  .brand-tagline {
    margin-top: 8px;
    font-family: "Cormorant Garamond", serif; font-style: italic; font-weight: 600;
    font-size: 22px; color: var(--teal);
  }
  .contact {
    position: absolute; left: 36px; bottom: 40px;
    list-style: none;
    font-family: "Cinzel", serif; font-size: 15px; color: #fff; letter-spacing: 0.5px;
  }
  .contact li { display: flex; align-items: center; gap: 10px; margin-top: 8px; }
  .contact svg { width: 16px; height: 16px; flex: none; }
  .person {
    position: absolute; right: 40px; bottom: 40px;
    text-align: right; color: #fff;
    font-family: "Cinzel", serif;
  }
  .person-name { font-size: 20px; letter-spacing: 1px; }
  .person-role { font-size: 14px; line-height: 1.5; margin-top: 6px; letter-spacing: 0.5px; }

  /* Back */
  .card-back { padding: 34px 44px; font-family: "Open Sans", sans-serif; color: var(--ink); }
  .appt-title { font-weight: 700; font-size: 19px; }
  .field { display: flex; align-items: flex-end; gap: 10px; margin-top: 22px; font-size: 16px; }
  .field .line { flex: 1; border-bottom: 1.5px solid var(--rule); height: 20px; }
  .field.name, .field.date { margin-left: 18px; }
  .days { display: flex; align-items: center; gap: 14px; margin-top: 26px; margin-left: 18px; font-size: 14px; }
  .day { display: flex; align-items: center; gap: 6px; }
  .box { width: 22px; height: 22px; border: 1.5px solid var(--rule); }
  .days .time { display: flex; align-items: flex-end; gap: 8px; flex: 1; margin-left: 6px; font-size: 16px; }
  .days .time .line { flex: 1; border-bottom: 1.5px solid var(--rule); height: 20px; }
  .policy { margin-top: 46px; }
  .policy-title { font-weight: 700; font-size: 15px; }
  .policy-text { font-style: italic; font-size: 14px; margin-top: 4px; }
</style>
</head>
<body>
<main class="canvas">

  <section class="card card-front" aria-label="Business card front">
    <svg class="wave" viewBox="0 0 760 434" preserveAspectRatio="none" aria-hidden="true">
      <path d="M0,232 C180,300 420,250 760,178 L760,196 C430,270 190,318 0,262 Z" fill="var(--sky-pale)"/>
      <path d="M0,250 C190,312 430,262 760,190" fill="none" stroke="var(--sky)" stroke-width="6"/>
      <path d="M0,262 C190,318 430,270 760,198 L760,434 L0,434 Z" fill="var(--navy)"/>
    </svg>

    <div class="brand">
      <span class="brand-mark"></span>
      <div>
        <div class="brand-name">BRIGHT WILLOW WELLNESS</div>
        <div class="brand-tagline">Achieve balanced health and well-being</div>
      </div>
    </div>

    <ul class="contact">
      <li>
        <svg viewBox="0 0 16 16"><path d="M4 1.5 L6.5 4.5 L5 6.2 C6 8.3 7.7 10 9.8 11 L11.5 9.5 L14.5 12 L13 14.5 C7 14 2 9 1.5 3 Z" fill="#fff"/></svg>
        (555) 014-2290
      </li>
      <li>
        <svg viewBox="0 0 16 16"><rect x="1" y="3.5" width="14" height="9" fill="none" stroke="#fff" stroke-width="1.4"/><path d="M1 3.5 L8 9 L15 3.5" fill="none" stroke="#fff" stroke-width="1.4"/></svg>
        melora@brightwillowwellness.example
      </li>
      <li>
        <svg viewBox="0 0 16 16"><circle cx="8" cy="8" r="6.5" fill="none" stroke="#fff" stroke-width="1.4"/><ellipse cx="8" cy="8" rx="3" ry="6.5" fill="none" stroke="#fff" stroke-width="1.2"/><path d="M1.5 8 H14.5" stroke="#fff" stroke-width="1.2"/></svg>
        www.brightwillowwellness.example
      </li>
    </ul>

    <div class="person">
      <div class="person-name">Melora T. Grant, MSW, LSW</div>
      <div class="person-role">Health Consultant and<br>Spiritual Counselor</div>
    </div>
  </section>

  <section class="card card-back" aria-label="Business card back">
    <h2 class="appt-title">Appointment</h2>
    <div class="field name">Name: <span class="line"></span></div>
    <div class="field date">Date: <span class="line"></span></div>
    <div class="days">
      <span class="day"><span class="box"></span>MON</span>
      <span class="day"><span class="box"></span>TUE</span>
      <span class="day"><span class="box"></span>WED</span>
      <span class="day"><span class="box"></span>THU</span>
      <span class="day"><span class="box"></span>FRI</span>
      <span class="day"><span class="box"></span>SAT</span>
      <span class="time">Time: <span class="line"></span></span>
    </div>
    <div class="policy">
      <div class="policy-title">Cancellation Policy</div>
      <p class="policy-text">We require 24 hours cancellation for appointments otherwise a charge may be incurred.</p>
    </div>
  </section>

</main>
</body>
</html>
```